Tarn - Stationary Design/Layout

We are a well established clothing design and manufacturing company (Tarn Sourcing) based in London UK, with our own factory in Bangladesh, supplying to many fashion retailers and brands. Our factory has very high environmental and ethical standards with people at its heart. Our quality of garments are second to none.
Our new logo has been proudly developed by the Pixel Guild community last month, we are now in the second phase and need the layout designed for our letterheads, double sided business cards, compliment slip and clothing ticket. Feel as creative as you like, but make sure it looks great!!
***The Logo - the logo design and colour is set and should NOT be changed and stay on a dark grey backround. The logo artwork to use is attached.
***Details to use for the business card:
Dorian Pelham
Direct Line: 020 7946 0158
dorian@tarnsourcing-example.com
Tarn Sourching Ltd.
57 - 59 Hollin Row
Ashgrove . Wendleby
NW9 4QT
Switchboard: 020 7946 0274
Fax: 020 7946 0274
www.tarnsourcing-example.co.uk
***Details to use for the letterhead and compliment slip:
Tarn Sourching Ltd.
57 - 59 Hollin Row
Ashgrove . Wendleby
NW9 4QT
Fax: 020 7946 0274
www.tarnsourcing-example.co.uk
***Details for Swing Ticket:
Size: 12cm height by 5.5cm width
One side need to have just the logo without the 'Sourcing', on the other it needs to stay blank

```html
<!DOCTYPE html>
<html lang="en">
<head>
<meta charset="utf-8">
<title>Tarn Sourcing Letterhead</title>
<link rel="stylesheet" href="https://fonts.googleapis.com/css2?family=Arimo:wght@400&display=swap">
<style>
  :root {
    --header-grey: #333333;
    --logo-cyan: #a9e2e0;
    --paper: #ffffff;
    --ink: #1a1a1a;
    --link-cyan: #a6dede;
    --tile-dark: #4a4f50;
    --tile-mid: #6f8c8c;
    --tile-light: #d8fbf9;
  }
  html, body {
    margin: 0;
    padding: 0;
    overflow: hidden;
    background: var(--paper);
  }
  .letterhead {
    position: relative;
    width: 927px;
    height: 1200px;
    background: var(--paper);
    font-family: "Arimo", Arial, sans-serif;
    overflow: hidden;
  }
  .letterhead__header {
    position: absolute;
    left: 0;
    top: 0;
    width: 927px;
    height: 104px;
    background: var(--header-grey);
  }
  .brand {
    position: absolute;
    left: 24px;
    top: 26px;
    width: 142px;
    color: var(--logo-cyan);
    font-weight: 400;
  }
  .brand__name {
    display: block;
    font-size: 40px;
    line-height: 38px;
    letter-spacing: 3px;
  }
  .brand__tagline {
    display: block;
    text-align: right;
    font-size: 10px;
    letter-spacing: 1.2px;
    margin-top: 1px;
  }
  .header-texture {
    position: absolute;
    left: 220px;
    top: 0;
    width: 640px;
    height: 104px;
    background: linear-gradient(90deg, var(--header-grey) 0%, var(--tile-dark) 25%, var(--tile-mid) 60%, var(--tile-light) 100%);
  }
  .letterhead__footer {
    position: absolute;
    left: 0;
    right: 0;
    top: 1158px;
    text-align: center;
    font-size: 10.4px;
    color: var(--ink);
    white-space: nowrap;
  }
  .footer__group {
    display: inline-block;
    padding: 3px 4px;
  }
  .footer__group + .footer__group {
    border-left: 1px solid var(--ink);
  }
  .footer__web {
    color: var(--link-cyan);
  }
</style>
</head>
<body>
  <div class="letterhead">
    <header class="letterhead__header">
      <div class="brand">
        <span class="brand__name">TARN</span>
        <span class="brand__tagline">SOURCING</span>
      </div>
      <div class="header-texture" role="img" aria-label="Decorative pattern of grey and aqua tiles fading to white"></div>
    </header>

    <footer class="letterhead__footer">
      <span class="footer__group">Tarn Sourching Ltd. • 57 - 59 Hollin Row</span><span class="footer__group">Ashgrove . Wendleby • NW9 4QT</span><span class="footer__group">Switchboard: 020 7946 0274 &nbsp;• &nbsp;Fax: 020 7946 0274</span><span class="footer__group footer__web">www.tarnsourcing-example.co.uk</span>
    </footer>
  </div>
</body>
</html>
```